ドレッシングのパッケージデザイン依頼
商品名:朝つゆ香るまろやかドレッシング
容器:スパウトピラー180ml

サイズについては添付の図面をご覧下さい。
赤系、緑系
最初に送って頂くのはJPEG形式でもイラストレーター形式でも構いませんが、採用させて頂いた場合はイラスレーター形式で納品をお願い致します。
ホテルロゴデータを添付いたします。
この度はたくさんのご応募ありがとうございました。想定以上の数のデザインが集まりどれも甲乙つけがたく嬉しい悲鳴を上げておりますが、選考するこちらも気合を入れて丁寧に1つ一つ拝見させて頂き、決めたいと思います。結果につきましては、少しお時間を頂いて「2月10日」に発表させて頂きます。
ご参加いただいた皆様、重ねて御礼申し上げます。ありがとうございました!
当選者はKu-Taro様のデザインで決定致しました。
修正依頼中の為当選の選択は終了しておりませんが、皆様にご報告申し上げます。
大変すばらしいデザインが多く、非常に悩みましたが、他社商品との「差別化」という意味で並べてみた時に目に付くというのが決めてとなりました。
sorakep様、たかせがわゆずは様のデザインを次点とさせていただきます。
必要な要素がすべて入っており申し分なかったのですが、上記の理由から次点とさせていただきます。
以上になります。
今回、ご応募いただきましたすべての皆様に御礼申し上げます。
本当にありがとうございました。
次の機会もぜひ、よろしくお願い致します。

非常に優れたデザインの中で、差別化という意味で並べてみた時の特徴的なデザインという事で選ばせて頂きました。次点作品は最後まで社内でも迷ったデザインです。今回は惜しくも選考から外れてしまいましたが、非常に優れたデザイナーさんであることは間違いないです。次回もぜひご参加宜しくお願い致します。

この度は弊社のドレッシングのパッケージデザインに応募して頂き誠にありがとうございます。
全ての作品をしっかりと見させていただきました。大変レベルの高いデザインばかりで正直1つに決めるのが難しい状況ではございました。今回選ばせて頂いたデザインは他社のドレッシングデザインで見られない特徴的なデザインであった点が評価されました。ぜひ次回のコンペの際もぜひご参加いただければと存じます。重ねて皆様に御礼申し上げます。ありがとうございました。

```html
<!DOCTYPE html>
<html lang="ja">
<head>
<meta charset="utf-8">
<title>朝つゆ香るまろやかドレッシング</title>
<link href="https://fonts.googleapis.com/css2?family=Noto+Sans+JP:wght@500;700;900&family=Cormorant+Garamond:wght@600&display=swap" rel="stylesheet">
<style>
  :root {
    --paper: #ffffff;
    --trim: #9a9a9a;
    --wood-light: #f3dfbf;
    --wood-mid: #dcb47f;
    --wood-dark: #b98550;
    --title-brown: #5b2f14;
    --band-brown: #6a3a1e;
    --accent-red: #e03a1e;
    --accent-orange: #ef8a1e;
    --veg-orange: #e8742c;
    --veg-green: #7fae3a;
    --veg-onion: #d99a4e;
  }
  * { box-sizing: border-box; margin: 0; padding: 0; }
  html, body { width: 744px; height: 1200px; overflow: hidden; background: var(--paper); }
  body { position: relative; font-family: "Noto Sans JP", sans-serif; }

  .trim-marks { position: absolute; inset: 0; }

  .label { position: absolute; left: 45px; top: 50px; width: 655px; height: 1103px; overflow: hidden; background: var(--paper); }

  .wood-photo {
    position: absolute; left: 0; top: 0; width: 100%; height: 690px;
    background:
      radial-gradient(ellipse 55% 60% at 50% 42%, rgba(255,248,236,0.85), rgba(255,248,236,0) 70%),
      linear-gradient(90deg, var(--wood-mid), var(--wood-light) 30%, var(--wood-light) 70%, var(--wood-dark));
  }

  .brand { position: absolute; top: 36px; left: 0; width: 100%; text-align: center; color: var(--title-brown); }
  .brand-dot { display: block; width: 34px; height: 34px; margin: 0 auto 8px; border-radius: 50%; background: var(--title-brown); }
  .brand-name { font-family: "Cormorant Garamond", serif; font-weight: 600; font-size: 19px; letter-spacing: 2px; line-height: 1.2; }
  .brand-place { font-family: "Cormorant Garamond", serif; font-weight: 600; font-size: 10px; letter-spacing: 3px; }

  .lead { position: absolute; top: 135px; width: 100%; text-align: center; color: var(--title-brown); font-weight: 700; font-size: 21px; line-height: 1.45; }

  .product-name { position: absolute; left: 0; top: 200px; width: 100%; color: var(--title-brown); font-weight: 900; text-align: center; }
  .product-name .line { display: block; font-size: 78px; line-height: 1.0; letter-spacing: 2px; margin-bottom: 2px; }
  .product-name .line-wide { display: block; font-size: 74px; line-height: 1.1; letter-spacing: 8px; margin-top: 14px; }

  .feature-band {
    position: absolute; left: 0; top: 690px; width: 100%; height: 38px;
    background: var(--band-brown); color: #fff; font-weight: 700; font-size: 17px;
    display: flex; align-items: center; padding-left: 26px; white-space: nowrap;
  }
  .feature-band .ratio { display: inline-block; background: #fff; color: var(--accent-red); font-weight: 900; font-size: 20px; padding: 0 6px; margin: 0 6px 0 8px; border-radius: 12px; }
  .feature-band .note { font-size: 10px; font-weight: 500; }

  .volume { position: absolute; left: 205px; top: 760px; color: var(--accent-orange); font-weight: 700; font-size: 32px; letter-spacing: 1px; }

  .veg-photo {
    position: absolute; left: 0; top: 800px; width: 100%; height: 303px;
    background:
      radial-gradient(circle at 88% 30%, var(--veg-orange) 0 14%, transparent 15%),
      radial-gradient(circle at 30% 62%, var(--veg-onion) 0 17%, transparent 18%),
      radial-gradient(circle at 72% 68%, var(--veg-onion) 0 16%, transparent 17%),
      radial-gradient(ellipse 22% 45% at 10% 70%, var(--veg-orange), transparent 70%),
      radial-gradient(ellipse 60% 55% at 45% 45%, var(--veg-green), transparent 75%),
      linear-gradient(#ffffff, #f5efe3);
  }

  .additive-free {
    position: absolute; left: 320px; top: 822px; height: 28px; padding: 0 18px;
    background: var(--accent-orange); color: #fff; font-weight: 700; font-size: 17px;
    display: flex; align-items: center; letter-spacing: 1px;
  }
</style>
</head>
<body>
  <svg class="trim-marks" width="744" height="1200" viewBox="0 0 744 1200" aria-hidden="true">
    <g stroke="var(--trim)" stroke-width="1" fill="none">
      <path d="M45 0V35 M0 50H30 M25 0V50 M0 30H45"/>
      <path d="M700 0V35 M744 50H714 M719 0V50 M744 30H700"/>
      <path d="M45 1200V1168 M0 1153H30 M25 1200V1153 M0 1173H45"/>
      <path d="M700 1200V1168 M744 1153H714 M719 1200V1153 M744 1173H700"/>
      <path d="M372 0V35 M340 20H404"/>
      <path d="M372 1200V1168 M340 1180H404"/>
      <path d="M0 600H30 M15 570V630"/>
      <path d="M744 600H714 M729 570V630"/>
    </g>
  </svg>

  <main class="label">
    <div class="wood-photo" role="img" aria-label="木目の板の上に置かれた木製のフォークとスプーンの写真"></div>

    <div class="brand">
      <span class="brand-dot"></span>
      <div class="brand-name">HOTEL<br>AURORA CREST</div>
      <div class="brand-place">SEASIDE</div>
    </div>

    <p class="lead">にんじん・玉ねぎ・セロリを<br>たっぷり使った</p>

    <h1 class="product-name">
      <span class="line">朝つゆ</span>
      <span class="line">香る</span>
      <span class="line">まろやか</span>
      <span class="line-wide">ドレッシング</span>
    </h1>

    <div class="feature-band">
      野菜の粒を感じる食感、野菜の割合:内容量の<span class="ratio">55%</span><span class="note">※当社調べ</span>
    </div>

    <div class="volume">180mℓ</div>

    <div class="veg-photo" role="img" aria-label="にんじん、玉ねぎ、セロリ、トマトの野菜写真"></div>

    <div class="additive-free">無添加・生ドレッシング</div>
  </main>
</body>
</html>
```